Wine Bottle Label

Project: New Label for Kestrel Wine

Sponsored by: Nine Orchards (nineorchards.example and Marlowe Wines, producer of Kestrel Wines)

Product Description:

Wine comes in both red (cabernet, zinfandel) and white (Chardonnay, Sauvignon Blanc). It is marketed to restaurants and mid priced retailers including Fresh Basket, etc.) Wine is priced between $17 - $20 per bottle. The wine is in the medium price category and is intended for mid market appeal.

_
Label Requirements:

• Noticeable among other labels when on a black bottle. White labels are most noticeable but all color choices are an option if the brand stands out and can be easily recognizable from 10 – 12ft.

• Has to appeal to Gen X - younger people. Contemporary. Must appeal to women who buy the majority of wine in the US.

• Has to be presentable at the dinner table...slightly sophisticated.

• Has to connect with the “Official Emblem of the Larkfield Nature League” Great White Wrenmere

• Bird is most often seen in grassy green pasture/meadows or wading in shallow water. Alone or in group.

• Has to fit on the bottle: Label size: 3 ½” H – 2 ¾” W

• Keep it Simple, lots of empty space

• Could be free form graphic design, illustrations, photos, etc.

• Could be abstract representation providing it connects to Egrets, e.g. stamp of foot which is gold embossed or similar.)

• Label must contain:

o Brand Name: Wrenmere
o Varietal: will vary (Cabernet Sauvignon, Chardonnay, Sauvignon Blanc, Zinfandel, etc.)
o Appellation: varies (Sonoma County, Napa Valley, California)
o Vintage: 2010, 2011, etc.

• Variations in label color/design are possible between varietals but brand should be consistent.

Back design must also be included. Example of current back with text is attached.

Industry/Entity Type

Graphic Design

Requirements
Must have
• Must have relationship with Wrenmere Bird - figuratively or literally
Has to fit on the bottle: Label size: 3 ½” H – 2 ¾” W
o Brand Name: Wrenmere

```html
<!DOCTYPE html>
<html lang="en">
<head>
<meta charset="utf-8">
<title>Wrenmere Wine – Label Range</title>
<link rel="stylesheet" href="https://fonts.googleapis.com/css2?family=Great+Vibes&family=Raleway:wght@500;600&display=swap">
<style>
  :root {
    --stage-light: #fbfbfb;
    --stage-dark: #dcdcdc;
    --gold-dark: #9a6a22;
    --gold: #d4a24a;
    --gold-light: #f3d88c;
    --silver-dark: #8a8a8a;
    --silver: #cfcfcf;
    --silver-light: #f4f4f4;
    --white: #ffffff;
    --band-ink: #3a2a14;

    --cab-bg: #fcd59c;
    --cab-accent: #f1a829;
    --char-bg: #6a0608;
    --char-accent: #a8121a;
    --sauv-bg: #403b39;
    --sauv-accent: #2c2826;
    --zin-bg: #403c3b;
    --zin-accent: #bdbdbd;
  }
  * { margin: 0; padding: 0; box-sizing: border-box; }
  html, body { width: 1200px; height: 1000px; overflow: hidden; }
  body {
    background: radial-gradient(ellipse at 50% 40%, var(--stage-light) 0%, var(--stage-dark) 100%);
    font-family: "Raleway", Arial, sans-serif;
    position: relative;
  }
  .label-range { position: absolute; inset: 0; }

  .label {
    --metal-dark: var(--gold-dark);
    --metal: var(--gold);
    --metal-light: var(--gold-light);
    position: absolute;
    top: 440px;
    width: 210px;
    height: 345px;
    overflow: hidden;
    background: var(--label-bg);
    box-shadow: 0 6px 18px rgba(0,0,0,0.18);
  }
  .label.label--cabernet   { left: 90px;  --label-bg: var(--cab-bg);  --accent: var(--cab-accent); }
  .label.label--chardonnay { left: 348px; --label-bg: var(--char-bg); --accent: var(--char-accent); }
  .label.label--sauvignon  { left: 622px; --label-bg: var(--sauv-bg); --accent: var(--sauv-accent); }
  .label.label--zinfandel  { left: 886px; --label-bg: var(--zin-bg);  --accent: var(--zin-accent);
                             --metal-dark: var(--silver-dark); --metal: var(--silver); --metal-light: var(--silver-light); }

  .brand-name {
    position: absolute;
    top: 48px; left: 0; right: 0;
    text-align: center;
    font-family: "Great Vibes", cursive;
    font-weight: 400;
    font-size: 46px;
    line-height: 1;
    color: var(--metal);
  }
  .bird-artwork {
    position: absolute;
    left: 10px; top: 128px;
    width: 108px; height: 217px;
    border-radius: 50% 50% 10% 10% / 30% 30% 5% 5%;
    background: radial-gradient(ellipse at 55% 50%, var(--white) 0%, var(--white) 25%, var(--accent) 60%, var(--label-bg) 100%);
  }
  .wine-details {
    position: absolute;
    left: 120px; top: 188px;
    width: 84px;
    color: var(--white);
  }
  .vintage {
    font-size: 12px; font-weight: 500; letter-spacing: 0.5px; line-height: 1.2;
  }
  .varietal {
    font-size: 12px; font-weight: 600; letter-spacing: 0.3px; line-height: 1.15;
    text-transform: uppercase;
    padding-bottom: 3px;
    border-bottom: 1px solid var(--white);
  }
  .appellation {
    font-family: "Great Vibes", cursive;
    font-size: 15px; line-height: 1.4;
  }
  .content-band {
    position: absolute;
    left: 0; right: 0; bottom: 10px;
    height: 16px;
    background: linear-gradient(90deg, var(--metal-dark), var(--metal-light) 40%, var(--metal) 70%, var(--metal-dark));
    display: flex;
    justify-content: space-between;
    align-items: center;
    padding: 0 10px 0 60px;
    font-size: 8px; font-weight: 500;
    color: var(--band-ink);
    letter-spacing: 0.3px;
  }
</style>
</head>
<body>
<main class="label-range">

  <section class="label label--cabernet">
    <h2 class="brand-name">Wrenmere</h2>
    <div class="bird-artwork" role="img" aria-label="White wading bird silhouette standing before orange floral swirls"></div>
    <div class="wine-details">
      <p class="vintage">2010</p>
      <p class="varietal">Cabernet Sauvignon</p>
      <p class="appellation">California</p>
    </div>
    <div class="content-band"><span>ALC 13.5% BY VOL</span><span>750ML</span></div>
  </section>

  <section class="label label--chardonnay">
    <h2 class="brand-name">Wrenmere</h2>
    <div class="bird-artwork" role="img" aria-label="White wading bird silhouette standing before deep red floral swirls"></div>
    <div class="wine-details">
      <p class="vintage">2011</p>
      <p class="varietal">Chardonnay</p>
      <p class="appellation">California</p>
    </div>
    <div class="content-band"><span>ALC 13.5% BY VOL</span><span>750ML</span></div>
  </section>

  <section class="label label--sauvignon">
    <h2 class="brand-name">Wrenmere</h2>
    <div class="bird-artwork" role="img" aria-label="White wading bird silhouette standing before dark charcoal floral swirls"></div>
    <div class="wine-details">
      <p class="vintage">2011</p>
      <p class="varietal">Sauvignon Blanc</p>
      <p class="appellation">California</p>
    </div>
    <div class="content-band"><span>ALC 13.5% BY VOL</span><span>750ML</span></div>
  </section>

  <section class="label label--zinfandel">
    <h2 class="brand-name">Wrenmere</h2>
    <div class="bird-artwork" role="img" aria-label="White wading bird silhouette standing before silver floral swirls"></div>
    <div class="wine-details">
      <p class="vintage">2011</p>
      <p class="varietal">Zinfandel</p>
      <p class="appellation">California</p>
    </div>
    <div class="content-band"><span>ALC 13.5% BY VOL</span><span>750ML</span></div>
  </section>

</main>
</body>
</html>
```